Web Header needed for an inspirational coaching company's website - ongoing work

We need a beautifully designed web header to replace my current one at my homepage on my website www.brekavol.com
There will be continuous work required for various creative work in the future if your work is selected.
I work with corporate professionals and executives to bring clarity and joy back to their career. It needs to be elegant, sophisticated, intelligent, but friendly and inspiring at the same time.
Brief and the sample header size are attached in my files
Thank you!
Target Market(s)
Corporate profesionals and executives
Industry/Entity Type
It Company
Colors
Designer to choose colors to be used in the design.
Look and feel
Each slider illustrates characteristics of the customer's brand and the style your logo design should communicate.

```html
<!DOCTYPE html>
<html lang="en">
<head>
<meta charset="utf-8">
<title>Clearwell – Header Concepts</title>
<link rel="stylesheet" href="https://fonts.googleapis.com/css2?family=Source+Sans+3:wght@400;600&display=swap">
<style>
  :root {
    --page-bg: #ffffff;
    --band-top: #8b584c;
    --band-bottom: #94351b;
    --text-light: #ffffff;
    --button-top: #a32e0e;
    --button-bottom: #6e1a05;
    --photo-hair: #2b2624;
    --photo-skin: #d9a88e;
    --photo-top: #ef6a3c;
  }
  * { box-sizing: border-box; margin: 0; padding: 0; }
  html, body {
    width: 1200px; height: 938px; overflow: hidden;
    background: var(--page-bg);
    font-family: "Source Sans 3", sans-serif;
    color: var(--text-light);
  }
  .header-band {
    position: absolute; left: 38px; width: 1125px; height: 408px;
    background: linear-gradient(180deg, var(--band-top) 0%, var(--band-bottom) 100%);
    overflow: hidden;
  }
  .header-band--portrait { top: 34px; }
  .header-band--text-only { top: 483px; }

  .brand-name {
    position: absolute; left: 38px; top: 43px;
    font-size: 22px; line-height: 26px; font-weight: 600; letter-spacing: 0.5px;
    color: var(--text-light);
  }
  .main-nav a {
    position: absolute; top: 46px;
    font-size: 17px; line-height: 20px; font-weight: 400; color: var(--text-light);
    text-decoration: none; white-space: nowrap;
  }

  .portrait-area {
    position: absolute; left: 120px; top: 96px; width: 240px; height: 312px;
    border-radius: 100px 100px 0 0;
    background:
      radial-gradient(ellipse 36% 28% at 58% 34%, var(--photo-skin) 0%, var(--photo-skin) 60%, transparent 100%),
      linear-gradient(180deg, var(--photo-hair) 0%, var(--photo-hair) 62%, var(--photo-top) 80%, var(--photo-top) 100%);
    opacity: 0.9;
  }

  .headline {
    position: absolute; transform: translateX(-50%);
    font-size: 77px; font-weight: 600; line-height: 1; white-space: nowrap;
    letter-spacing: 0.5px;
  }
  .tagline {
    position: absolute; transform: translateX(-50%);
    font-size: 34px; font-weight: 600; line-height: 1; white-space: nowrap;
  }
  .header-band--portrait .headline { left: 732px; top: 145px; }
  .header-band--portrait .tagline { left: 727px; top: 252px; }
  .header-band--text-only .headline { left: 536px; top: 141px; }
  .header-band--text-only .tagline { left: 530px; top: 256px; }

  .contact-button {
    position: absolute; left: 903px; top: 338px; width: 188px; height: 54px;
    border: 2px solid var(--text-light); border-radius: 8px;
    background: linear-gradient(180deg, var(--button-top) 0%, var(--button-bottom) 100%);
    box-shadow: 0 3px 4px rgba(0,0,0,0.35);
    display: flex; align-items: center; justify-content: center;
    font-size: 32px; font-weight: 600; color: var(--text-light);
    text-decoration: none; letter-spacing: 0.5px;
  }
</style>
</head>
<body>

<header class="header-band header-band--portrait">
  <div class="portrait-area" role="img" aria-label="Portrait photo of the coach, smiling, with long dark hair and an orange top"></div>
  <div class="brand-name">Clearwell</div>
  <nav class="main-nav">
    <a href="#" style="left:185px">Home</a>
    <a href="#" style="left:266px">About Lian Wei</a>
    <a href="#" style="left:399px">Testimonial</a>
    <a href="#" style="left:520px">Methodology</a>
    <a href="#" style="left:654px">Coaching &amp; Mentoring</a>
    <a href="#" style="left:851px">Workshop</a>
    <a href="#" style="left:954px">Corporate</a>
    <a href="#" style="left:1063px">Blog</a>
  </nav>
  <h1 class="headline">Your Career Partner</h1>
  <p class="tagline">Bring Clarity to Your Career</p>
  <a class="contact-button" href="#">CONTACT</a>
</header>

<header class="header-band header-band--text-only">
  <div class="brand-name">Clearwell</div>
  <nav class="main-nav">
    <a href="#" style="left:185px">Home</a>
    <a href="#" style="left:266px">About Lian Wei</a>
    <a href="#" style="left:399px">Testimonial</a>
    <a href="#" style="left:520px">Methodology</a>
    <a href="#" style="left:654px">Coaching &amp; Mentoring</a>
    <a href="#" style="left:851px">Workshop</a>
    <a href="#" style="left:954px">Corporate</a>
    <a href="#" style="left:1063px">Blog</a>
  </nav>
  <h1 class="headline">Your Career Partner</h1>
  <p class="tagline">Bring Clarity to Your Career</p>
  <a class="contact-button" href="#">CONTACT</a>
</header>

</body>
</html>
```